Bref créative
Turnip Cuddler LLC
Embracing More Plant-Based Eating for Everyone
Bright & Fun-filled
Paula J. Mercer
Health & Wellness Coach, NQRS Certified
418 Marlow Ln.
Georgetown, KY 40871
theturnipcuddler@mailnest.example
www.turnipcuddler.example
http://twitter.com/TurnipCuddler
I do not want to have the address on the card.
Just the logo?

```html
<!DOCTYPE html>
<html lang="en">
<head>
<meta charset="utf-8">
<title>Turnip Cuddler — Business Card</title>
<link rel="stylesheet" href="https://fonts.googleapis.com/css2?family=Open+Sans:ital,wght@0,400;0,600;0,700;1,600&display=swap">
<style>
  :root {
    --backdrop: #3a3a3a;
    --card: #ffffff;
    --green-deep: #2f8a2a;
    --green-light: #8cc63f;
    --brown: #6b4a35;
    --ink: #333333;
    --rule: #c8c8c8;
  }
  * { margin: 0; padding: 0; box-sizing: border-box; }
  html, body {
    width: 1200px; height: 780px; overflow: hidden;
    background: var(--backdrop);
    font-family: "Open Sans", Arial, sans-serif;
  }
  .business-card {
    position: absolute; left: 100px; top: 90px;
    width: 1000px; height: 600px;
    background: var(--card);
    border-radius: 28px;
    overflow: hidden;
    box-shadow: 0 14px 30px rgba(0,0,0,.45);
  }
  .card-swoosh { position: absolute; inset: 0; }
  .brand {
    position: absolute; top: 150px; left: 0; right: 0;
    display: flex; justify-content: center; align-items: center; gap: 18px;
  }
  .brand-dot {
    width: 46px; height: 46px; border-radius: 50%;
    background: var(--green-deep);
  }
  .brand-name {
    font-weight: 700; font-size: 82px; letter-spacing: -1px;
    color: var(--green-deep); line-height: 1;
  }
  .divider {
    position: absolute; left: 508px; top: 280px;
    width: 2px; height: 130px; background: var(--rule);
  }
  .person {
    position: absolute; right: 512px; top: 332px; text-align: right;
  }
  .person-name {
    font-weight: 700; font-size: 30px; color: var(--green-deep);
  }
  .person-title {
    font-style: italic; font-weight: 600; font-size: 19px; color: var(--brown);
    margin-top: 2px;
  }
  .contacts {
    position: absolute; left: 526px; top: 278px;
    list-style: none; font-size: 20px; color: var(--ink);
  }
  .contacts li {
    display: flex; align-items: center; gap: 12px; height: 33px;
  }
  .contact-icon {
    width: 22px; height: 22px; flex: none;
    display: flex; align-items: center; justify-content: center;
  }
  .contact-icon--at {
    color: var(--green-deep); font-weight: 700; font-size: 22px;
  }
  .icon-square {
    width: 20px; height: 20px; border-radius: 4px; background: var(--green-deep);
  }
</style>
</head>
<body>
  <div class="business-card">
    <svg class="card-swoosh" viewBox="0 0 1000 600" preserveAspectRatio="none" aria-hidden="true">
      <defs>
        <linearGradient id="band" x1="0" y1="0" x2="0" y2="1">
          <stop offset="0" stop-color="#8cc63f"/>
          <stop offset="1" stop-color="#2f8a2a"/>
        </linearGradient>
      </defs>
      <path d="M0 505 C 300 490, 650 500, 1000 430 L1000 600 L0 600 Z" fill="url(#band)"/>
      <path d="M0 488 C 300 472, 650 482, 1000 412" fill="none" stroke="#6b4a35" stroke-width="7"/>
    </svg>

    <div class="brand">
      <span class="brand-dot"></span>
      <span class="brand-name">Turnip Cuddler</span>
    </div>

    <div class="divider"></div>

    <div class="person">
      <div class="person-name">Paula J. Mercer</div>
      <div class="person-title">Health &amp; Wellness Coach, NQRS Certified</div>
    </div>

    <ul class="contacts">
      <li>
        <span class="contact-icon">
          <svg width="20" height="20" viewBox="0 0 24 24" aria-hidden="true"><path fill="#2f8a2a" d="M6.6 10.8a15.1 15.1 0 0 0 6.6 6.6l2.2-2.2a1 1 0 0 1 1-.25 11.4 11.4 0 0 0 3.6.57 1 1 0 0 1 1 1V20a1 1 0 0 1-1 1A17 17 0 0 1 3 4a1 1 0 0 1 1-1h3.5a1 1 0 0 1 1 1c0 1.25.2 2.45.57 3.57a1 1 0 0 1-.25 1z"/></svg>
        </span>
        859-555-0143
      </li>
      <li>
        <span class="contact-icon contact-icon--at">@</span>
        theturnipcuddler@mailnest.example
      </li>
      <li>
        <span class="contact-icon">
          <svg width="20" height="20" viewBox="0 0 24 24" aria-hidden="true"><circle cx="12" cy="12" r="10" fill="#2f8a2a"/><path d="M2 12h20M12 2c3 3 3 17 0 20M12 2c-3 3-3 17 0 20" fill="none" stroke="#fff" stroke-width="1.5"/></svg>
        </span>
        www.i-love-my-rugs.example
      </li>
      <li>
        <span class="contact-icon"><span class="icon-square"></span></span>
        chirper.example/TurnipCuddler
      </li>
    </ul>
  </div>
</body>
</html>
```